Property lawyer needs a website for new law firm Sydney

WHO AM I ?
I am a real estate development lawyer based in suburban Sydney Australia with over 14 years experience and have recently started my own law firm "Bramblewood Legal". The firm is just me (a female) at this stage. I need a website designed that is capable of being edited by me frequently (hoping this is easily done?!) and can be published with the domain name I own - www.bramblewoodlegal.com.au.
My areas of practice are:
* Property development (strata & community titling, due diligence, easements, by-laws and management statements, structuring etc)
* Conveyancing (sale and purchase of residential, commercial and retail property)
* General property law (caveats, transfers, related party transactions, easements, leases, powers of attorney etc).
WEBSITE REQUIREMENTS
I would like a website which conveys professionalism, has a fresh modern corporate look and is easy to navigate. The website will mostly be accessed by potential clients looking for information about me, my areas of practice and how to get in contact with me. My potential clients are corporate developers and individuals who are buying and selling property.
My logo for Bramblewood Legal (see attached) is simple, clean and professional looking. I would like the website to work with the logo without being too dark.
I haven't written all of the content yet, so please use filler text for everything and structure the menus as described above. The site will need to be capable of being updated and edited by me.
Other than that I will leave the design up to you.
Thanks and happy designing!
Target Market(s)
Professional developers and individuals buying and selling real estate
Industry/Entity Type
Real Estate
Coding
Coded - Design and coding required
Number of Pages Required
4 page
Requirements
Must have
- I would like a website which conveys professionalism, has a fresh modern corporate look and is easy to navigate. The website will mostly be accessed by potential clients looking for information about me, my areas of practice and how to get in contact with me. My potential clients are corporate developers and individuals who are buying and selling property.
- Please use my logo for Bramblewood Legal. I would like the website to work with the logo - the colours are a dark blue (C 100% M 50% B 50%) and grey (C10% B 40%). I don't want the website to be too dark though.
- I am thinking 4 pages. I would like links across the top of the page for "Practice Areas", "About us" and "Contact us" - these should lead to separate landing pages with the content to be inserted later.
- The contact page should contain space for a potential client to send an email enquiry to the following email address "enquiries@bramblewoodlegal.com.au". My contact details are set out in the attached letterhead (see attached).
- I would also like the home page to set out what my three Practice Areas are - Property Development; Conveyancing; General Property Law. Each area should have some filler text under it which will be completed later and a link to be able to take me to the "Practice Areas" page where more detail on each will be provided.
- Please select images that are relevant to my practice as a property lawyer. The photos you use will be the ones which I use so please choose wisely.
- I will need a link on the bottom of the home page showing that I am a member of "The Counsel Guild of NSW" (see attached logo).
- The bottom of each page should also include the following statement "Bramblewood Legal is a business name of Bramblewood Legal Pty Limited ACN 482 517 306, an incorporated legal practice regulated by the Legal Profession Act 2004. Liability limited by a scheme approved under the Professional Standards Legislation."
Nice to have
- Have attached an image of me (not the best) but at least its me. Consider whether to use on "About us" page
Should not have
- No images of gavels, scales of justice or law books.
- Images not to be too masculine
- Website not to be too dark

```html
<!DOCTYPE html>
<html lang="en">
<head>
<meta charset="utf-8">
<title>Bramblewood Legal</title>
<link rel="stylesheet" href="https://fonts.googleapis.com/css2?family=Arimo:wght@400;700&family=Roboto+Slab:wght@600&display=swap">
<style>
:root{
  --page:#ededec;
  --brand:#13456f;
  --nav-text:#7a7a7a;
  --pill-top:#3b45a0;
  --pill-bottom:#1d2470;
  --frame-dark:#0b1c2c;
  --frame-teal:#1c5d70;
  --sky-top:#2f5596;
  --sky-mid:#6f93c8;
  --sky-low:#c9daef;
  --band-edge:#3a44a8;
  --card:#ffffff;
  --muted:#a8a8a8;
  --body-text:#555;
  --ink:#111;
}
*{box-sizing:border-box;margin:0;padding:0}
html,body{width:1200px;height:888px;overflow:hidden}
body{background:var(--page) radial-gradient(ellipse at 50% 30%,#f3f3f2 0%,#e6e6e4 100%);font-family:Arimo,Arial,sans-serif;position:relative}
.logo{position:absolute;left:183px;top:47px;font-weight:700;font-size:22px;letter-spacing:-.6px;color:var(--brand);text-transform:uppercase;white-space:nowrap}
.main-nav{position:absolute;top:45px;left:617px;display:flex;align-items:center}
.main-nav a{font-family:"Roboto Slab",Georgia,serif;font-weight:600;font-size:13.5px;color:var(--nav-text);text-decoration:none;height:26px;line-height:26px;text-align:center}
.main-nav a:nth-child(1){width:101px}
.main-nav a:nth-child(2){width:80px;margin-left:14px}
.main-nav a:nth-child(3){width:90px;margin-left:12px}
.main-nav a:nth-child(4){width:100px}
.main-nav a.active{color:#fff;background:linear-gradient(var(--pill-top),var(--pill-bottom));border-radius:8px;box-shadow:0 0 0 1px #141a55 inset}
.hero{position:absolute;left:182px;top:129px;width:845px;height:395px;border-radius:5px 0 0 5px;background:linear-gradient(90deg,var(--frame-dark) 0%,#0f2a3c 60%,var(--frame-teal) 100%)}
.hero-photo{position:absolute;left:17px;top:23px;width:810px;height:352px;border-radius:4px 4px 0 0;background:linear-gradient(180deg,var(--sky-top) 0%,var(--sky-mid) 45%,var(--sky-low) 100%)}
.hero-rule{position:absolute;left:185px;top:559px;width:842px;height:1px;background:#222}
.hero-rule-soft{position:absolute;left:178px;top:568px;width:852px;height:1px;background:#dcdcdb}
.content-card{position:absolute;left:199px;top:605px;width:811px;height:240px;background:var(--card);border:1px solid #ddd;border-radius:3px;box-shadow:0 3px 6px rgba(0,0,0,.08)}
.practice-areas{position:absolute;left:14px;top:16px;width:781px;display:flex;gap:24px}
.practice-area{flex:1}
.practice-area h2{font-size:13px;font-weight:700;color:var(--brand);margin-bottom:5px}
.practice-area p{font-size:11px;line-height:14px;color:var(--body-text);margin-bottom:5px}
.practice-area a{font-size:11px;color:var(--pill-top);text-decoration:none;font-weight:700}
.footer-band{position:absolute;left:182px;top:724px;width:845px;height:67px}
.footer-band svg{position:absolute;left:0;top:0}
.footer-logo{position:absolute;left:26px;top:20px;font-weight:700;font-size:18px;letter-spacing:-.4px;color:var(--brand);text-transform:uppercase;white-space:nowrap}
.guild-link{position:absolute;left:330px;top:22px;display:flex;align-items:center;gap:7px;font-size:11px;color:#fff;text-decoration:none;white-space:nowrap}
.guild-badge{width:14px;height:14px;background:#fff;border-radius:2px;opacity:.9}
.social{position:absolute;top:19px;display:block;width:22px;height:22px;background:var(--frame-dark);border-radius:2px}
.footer-nav{position:absolute;left:0;top:798px;width:1200px;text-align:center;font-size:8.5px;color:var(--muted)}
.footer-nav a{color:var(--muted);text-decoration:none;margin:0 9px}
.liability{position:absolute;left:230px;top:812px;width:740px;text-align:center;font-size:8.5px;line-height:11px;color:#8a8a8a}
.copyright{position:absolute;left:0;top:856px;width:1200px;text-align:center;font-size:8.5px;color:#8a8a8a}
</style>
</head>
<body>
<div class="logo">Bramblewood Legal</div>
<nav class="main-nav">
  <a class="active" href="#">Home</a>
  <a href="#">About</a>
  <a href="#">Contact</a>
  <a href="#">Prac. Areas</a>
</nav>

<section class="hero">
  <div class="hero-photo" role="img" aria-label="Photo of two business people shaking hands against blue sky and office towers"></div>
</section>
<div class="hero-rule"></div>
<div class="hero-rule-soft"></div>

<main class="content-card">
  <div class="practice-areas">
    <article class="practice-area">
      <h2>Property Development</h2>
      <p>Strata and community titling, due diligence, easements, by-laws and project structuring.</p>
      <a href="#">Read more ›</a>
    </article>
    <article class="practice-area">
      <h2>Conveyancing</h2>
      <p>Sale and purchase of residential, commercial and retail property, handled with care.</p>
      <a href="#">Read more ›</a>
    </article>
    <article class="practice-area">
      <h2>General Property Law</h2>
      <p>Caveats, transfers, related party transactions, leases and powers of attorney.</p>
      <a href="#">Read more ›</a>
    </article>
  </div>
</main>

<footer class="footer-band">
  <svg width="845" height="67" viewBox="0 0 845 67" aria-hidden="true">
    <defs>
      <linearGradient id="band" x1="0" y1="0" x2="0" y2="1">
        <stop offset="0" stop-color="#8d9cf0"/>
        <stop offset="1" stop-color="#5f6fd9"/>
      </linearGradient>
    </defs>
    <path d="M0 58 Q0 66 12 66 L18 58 Z M845 58 Q845 66 833 66 L827 58 Z" fill="#2a3290"/>
    <rect x="0.5" y="0.5" width="844" height="58" rx="4" fill="url(#band)" stroke="#3a44a8"/>
    <rect x="2" y="2" width="841" height="2" fill="#b4bff7"/>
  </svg>
  <div class="footer-logo">Bramblewood Legal</div>
  <a class="guild-link" href="#"><span class="guild-badge"></span>Member of The Counsel Guild of NSW</a>
  <a class="social" style="left:699px" href="#" aria-label="Social profile one"></a>
  <a class="social" style="left:743px;border-radius:50%" href="#" aria-label="Social profile two"></a>
  <a class="social" style="left:790px" href="#" aria-label="Social profile three"></a>
</footer>

<nav class="footer-nav">
  <a href="#">Home</a>|<a href="#">About</a>|<a href="#">Contact</a>|<a href="#">Prac. Areas</a>
</nav>
<p class="liability">Bramblewood Legal is a business name of Bramblewood Legal Pty Limited ACN 482 517 306, an incorporated legal practice regulated by the Legal Profession Act 2004. Liability limited by a scheme approved under the Professional Standards Legislation.</p>
<div class="copyright">© Copyright © 2015 BRAMBLEWOODLEGAL all rights reserved</div>
</body>
</html>
```